Brannigan Ashcroft LLC. custom built/handcrafted

I am recent small business owner looking to sell my art(drawings) and woodworking projects from my home. I have a very rough draft of a simple card design created on a simple digital program. I was hoping for a fancier lettering on the initial letters (BA). More of a calligraphy style. Also, the yellow border around the logo I would like to be a gold foil look. For it to be shiny or reflective look and to keep the other letters black with a consistent font on the card and the card white.

Target Market(s)

Local and neighboring cities

Industry/Entity Type

Art (drawing)/Woodworking

Contact Information for Business Card

My email tpashcroft@mailvane.net, phone number 949-517-3068. In the files provided it has a yellow border around the logo and I was looking to make that a gold foil.

Font styles to use
Serif
Decorative
Script

Requirements
Nice to have
• symbols for having a Facebook and Instagram

```html
<!DOCTYPE html>
<html lang="en">
<head>
<meta charset="utf-8">
<title>Brannigan Ashcroft LLC. Business Card</title>
<link rel="stylesheet" href="https://fonts.googleapis.com/css2?family=Poppins:wght@300;400;500;600&display=swap">
<style>
  :root {
    --backdrop: #d4d4d6;
    --card: #f7f7f6;
    --ink: #1c1c1c;
    --rule: #3a3a3a;
    --foil-copper: #c2601c;
    --foil-gold: #e9b92c;
    --foil-light: #f3ec86;
  }
  * { box-sizing: border-box; margin: 0; padding: 0; }
  html, body {
    width: 1200px;
    height: 900px;
    overflow: hidden;
    background: var(--backdrop);
    font-family: "Poppins", sans-serif;
    color: var(--ink);
  }
  .stage {
    width: 1200px;
    height: 900px;
    display: flex;
    align-items: center;
    justify-content: center;
    gap: 44px;
  }
  .card {
    position: relative;
    width: 520px;
    height: 297px;
    background: var(--card);
    box-shadow: 0 6px 18px rgba(0, 0, 0, 0.12);
  }

  /* Front: contact side */
  .card--front {
    display: flex;
    flex-direction: column;
    align-items: center;
    padding-top: 56px;
  }
  .owner-name {
    font-weight: 600;
    font-size: 24px;
    letter-spacing: 0.3px;
    line-height: 1.1;
  }
  .owner-title {
    font-weight: 300;
    font-size: 12px;
    letter-spacing: 1.5px;
    margin-top: 2px;
  }
  .contact-divider {
    display: flex;
    align-items: center;
    gap: 8px;
    margin-top: 18px;
  }
  .contact-divider__line {
    width: 84px;
    height: 1.5px;
    background: var(--rule);
  }
  .contact-icon {
    width: 24px;
    height: 24px;
    border-radius: 50%;
    background: var(--ink);
    display: flex;
    align-items: center;
    justify-content: center;
  }
  .contact-icon svg { width: 13px; height: 13px; }
  .contact-details {
    margin-top: 14px;
    text-align: center;
    font-weight: 300;
    font-size: 17px;
    line-height: 1.3;
    letter-spacing: 0.4px;
  }
  .social-row {
    display: flex;
    gap: 6px;
    margin-top: 12px;
  }
  .social-dot {
    width: 24px;
    height: 24px;
    border-radius: 50%;
    background: var(--ink);
  }

  /* Back: brand side */
  .card--back .foil-frame {
    position: absolute;
    inset: 0;
    width: 100%;
    height: 100%;
  }
  .brand-lockup {
    position: absolute;
    inset: 0;
    display: flex;
    align-items: center;
    justify-content: center;
  }
  .brand-name {
    font-weight: 500;
    font-size: 22px;
    letter-spacing: 1.5px;
    text-transform: uppercase;
    color: var(--ink);
  }
</style>
</head>
<body>
<main class="stage">

  <section class="card card--front" aria-label="Business card, contact side">
    <h1 class="owner-name">Thomas P. Ashcroft</h1>
    <p class="owner-title">OWNER</p>

    <div class="contact-divider">
      <span class="contact-divider__line"></span>
      <span class="contact-icon" aria-label="Phone">
        <svg viewBox="0 0 24 24" fill="#ffffff">
          <path d="M6.6 10.8c1.4 2.8 3.8 5.1 6.6 6.6l2.2-2.2c.3-.3.7-.4 1-.2 1.1.4 2.3.6 3.6.6.6 0 1 .4 1 1V20c0 .6-.4 1-1 1C10.6 21 3 13.4 3 4c0-.6.4-1 1-1h3.5c.6 0 1 .4 1 1 0 1.3.2 2.5.6 3.6.1.3 0 .7-.2 1L6.6 10.8z"/>
        </svg>
      </span>
      <span class="contact-icon" aria-label="Email">
        <svg viewBox="0 0 24 24" fill="none" stroke="#ffffff" stroke-width="2" stroke-linejoin="round">
          <rect x="3" y="5.5" width="18" height="13" rx="1.5" fill="#ffffff" stroke="none"/>
          <path d="M3.5 6.5 12 13l8.5-6.5" stroke="#1c1c1c" stroke-width="1.6"/>
        </svg>
      </span>
      <span class="contact-divider__line"></span>
    </div>

    <p class="contact-details">
      949-517-3068<br>
      tpashcroft@mailvane.net
    </p>

    <div class="social-row" aria-label="Social media">
      <span class="social-dot"></span>
      <span class="social-dot"></span>
    </div>
  </section>

  <section class="card card--back" aria-label="Business card, brand side">
    <svg class="foil-frame" viewBox="0 0 520 297" aria-hidden="true">
      <defs>
        <linearGradient id="goldFoil" x1="0" y1="1" x2="1" y2="0">
          <stop offset="0" stop-color="var(--foil-copper)"/>
          <stop offset="0.35" stop-color="var(--foil-copper)"/>
          <stop offset="0.6" stop-color="var(--foil-gold)"/>
          <stop offset="0.8" stop-color="var(--foil-light)"/>
          <stop offset="1" stop-color="var(--foil-gold)"/>
        </linearGradient>
      </defs>
      <rect x="66" y="40" width="388" height="217" fill="none" stroke="url(#goldFoil)" stroke-width="4.5"/>
    </svg>
    <div class="brand-lockup">
      <p class="brand-name">Brannigan Ashcroft</p>
    </div>
  </section>

</main>
</body>
</html>
```